Marketing Brochure: Category Management – Assortment Optimization

Create a compelling a 1-page marketing brochure around a service that allows Brill International retailers to optimize their product assortments in their stores. The brochure must be fun, very professionally done, clean, and exciting to want possible clients to want to pick up. See word file for content details. The Brill Worldwide Partners red and white colors should be used. Also, include relevant photos to liven up the brochure.

Target Market(s)

Brill Toolworks Retailers in Different Parts of the World

Industry/Entity Type

Retail

Font styles to use
Sans Serif

Requirements
Must have
• See Word file. Add some really good photos relevant to retail.
• Red and White Colors would be good to match Brill Worldwide Partners logo
• Also, should look like a 'global' service. Maybe add a worldly look to it.
Nice to have
• See World file
Should not have
• N/A

```html
<!DOCTYPE html>
<html lang="en">
<head>
<meta charset="utf-8">
<title>Brill Worldwide Partners – Category Management Flyer</title>
<link href="https://fonts.googleapis.com/css2?family=Lato:wght@300;400;700;900&family=Oswald:wght@600&display=swap" rel="stylesheet">
<style>
  :root {
    --brand-red: #e8322b;
    --ink: #2d2d2d;
    --body-ink: #3a3a3a;
    --panel-grey: #efeeec;
    --title-bar: #4a4849;
    --page-bg: #ece9e4;
    --white: #ffffff;
  }
  * { box-sizing: border-box; margin: 0; padding: 0; }
  html, body { width: 1200px; height: 1200px; overflow: hidden; }
  body {
    background: var(--page-bg);
    font-family: "Lato", sans-serif;
    color: var(--body-ink);
    position: relative;
  }
  .flyer {
    position: absolute;
    left: 190px; top: 20px;
    width: 820px; height: 1160px;
    background: var(--white);
    overflow: hidden;
  }
  .hero-photo {
    position: absolute; left: 0; top: 0;
    width: 820px; height: 400px;
    background:
      linear-gradient(115deg, rgba(255,255,255,0) 45%, rgba(120,150,185,0.55) 60%, rgba(90,125,165,0.7) 80%, rgba(190,205,220,0.5) 100%),
      linear-gradient(180deg, #c9d3dc 0%, #dde3e8 45%, #e9ecee 100%);
  }
  .brand {
    position: absolute; left: 48px; top: 52px;
    display: flex; align-items: center; gap: 12px;
  }
  .brand-dot {
    width: 40px; height: 40px; border-radius: 50%;
    background: var(--brand-red);
  }
  .brand-name {
    font-weight: 900; font-size: 26px; letter-spacing: 0.5px;
    color: var(--ink); text-transform: uppercase;
  }
  .title-bar {
    position: absolute; left: 48px; top: 290px;
    padding: 14px 26px;
    background: var(--title-bar);
  }
  .title-bar h1 {
    font-weight: 400; font-size: 28px; line-height: 1.25;
    color: var(--white); white-space: nowrap;
  }
  .title-bar h1 .accent { display: block; color: var(--brand-red); padding-left: 140px; }
  .hero-rule {
    position: absolute; left: 0; top: 400px;
    width: 820px; height: 7px; background: var(--brand-red);
  }
  .intro {
    position: absolute; left: 60px; top: 426px; width: 700px;
    text-align: center; font-size: 13px; line-height: 1.5;
  }
  .intro p + p { margin-top: 12px; }
  .columns {
    position: absolute; left: 24px; right: 24px; top: 610px; bottom: 92px;
    display: grid; grid-template-columns: 370px 378px; column-gap: 24px;
    align-items: start;
  }
  .panel { background: var(--panel-grey); padding: 20px 24px 22px; }
  .panel-roi { margin-top: 22px; }
  .panel h2 {
    font-family: "Oswald", sans-serif; font-weight: 600;
    font-size: 23px; line-height: 1.2; color: var(--ink); text-transform: uppercase;
    display: flex; align-items: center; gap: 10px; margin-bottom: 10px;
  }
  .panel-roi h2 { justify-content: center; }
  .panel h2 svg { flex: none; }
  .panel p { font-size: 15px; line-height: 1.42; color: var(--body-ink); }
  .panel-roi p { text-align: center; }
  .right-col { display: flex; flex-direction: column; gap: 14px; }
  .feature { text-align: center; padding: 0 6px; }
  .feature h2 {
    font-weight: 900; font-size: 23px; line-height: 1.2; text-transform: uppercase;
    margin-bottom: 6px; white-space: nowrap;
  }
  .feature h2 .red { color: var(--brand-red); }
  .feature h2 .dark { color: var(--ink); }
  .feature p { font-size: 12.5px; line-height: 1.45; }
  .footer-band {
    position: absolute; left: 0; bottom: 0;
    width: 820px; height: 80px; background: var(--brand-red);
    display: flex; align-items: center; justify-content: flex-end;
    padding-right: 40px;
  }
  .footer-band .web {
    font-weight: 300; font-size: 40px; color: var(--white); letter-spacing: 1px;
  }
</style>
</head>
<body>
  <main class="flyer">
    <div class="hero-photo" role="img" aria-label="Photo of a glass skyscraper rising into a cloudy blue sky"></div>

    <div class="brand">
      <span class="brand-dot"></span>
      <span class="brand-name">Brill Worldwide Partners</span>
    </div>

    <div class="title-bar">
      <h1>Satisfying Customers with Data-Driven <span class="accent">Informed Decisions</span></h1>
    </div>

    <div class="hero-rule"></div>

    <section class="intro">
      <p>It takes a strong category strategy to drive sales growth. With changes in consumer demands and product introductions constantly making their way into the market, it's not easy to optimize product selection toward maximizing market share and wider profit margins. To do so, companies need to quickly and effectively deploy well-established and nimble methodologies that refine and enhance category assortment and retail space decisions.</p>
      <p>Brill Worldwide Partners category management's monthly services provides your business industry expertise, functional richness, and retail data analytics know-how to drive more profitable and productive product assortments. We speak analytics. In doing so, we synthesize raw data, assess it, and covert it into practical, measured solutions to help your business grow.</p>
    </section>

    <div class="columns">
      <section class="panel panel-roi">
        <h2>Return on Investment
          <svg width="24" height="24" viewBox="0 0 24 24" aria-hidden="true">
            <circle cx="12" cy="12" r="12" fill="#e8322b"/>
            <path d="M6 16 L11 11 L14 14 L18 8 M14.5 8 H18 V11.5" stroke="#fff" stroke-width="2" fill="none" stroke-linecap="round" stroke-linejoin="round"/>
          </svg>
        </h2>
        <p>Increased profitability and turnover. Simplify assortments and planograms create a more consumer-friendly shopping experience. Attack over-SKU'd categories and less duplication. Fact-based analytics with collaborative market insights. Reduce wasteful spending and to help brands help retailers compete more effectively. Acquired processes are safeguarded for the long-term. The customer remains at the heart of decision making.</p>
      </section>

      <div class="right-col">
        <section class="panel panel-approach">
          <h2>
            <svg width="24" height="24" viewBox="0 0 24 24" aria-hidden="true">
              <circle cx="12" cy="12" r="12" fill="#e8322b"/>
              <path d="M7 7 L17 17 M17 7 L7 17" stroke="#fff" stroke-width="2.4" stroke-linecap="round"/>
            </svg>
            Our Service Approach
          </h2>
          <p>Understand your long-term vision, market and assortment objectives. Assess the current state of affairs to your categories. Obtain store level raw data one category at a time. Covert raw data into powerful insights about category performance, opportunities, potential impact, and goal setting. Implement recommendations, track results, and further advise.</p>
        </section>

        <section class="feature">
          <h2><span class="red">Business</span> <span class="dark">Service</span> <span class="red">Feature</span></h2>
          <p>Brill Worldwide Partners is a Brill Toolworks International consulting service that provides training and strategy recommendations based on Brill's 94-year retail industry expertise. Our services drive significant and sustainable performance improvements so you can accomplish your company's most important business objectives.</p>
        </section>
      </div>
    </div>

    <footer class="footer-band">
      <span class="web">www.yourwebsite.com</span>
    </footer>
  </main>
</body>
</html>
```